Full Page Ad

We are like looking for something modern, Rustic and unique for a full page ad that includes our logo, office locations, contact information. Please see our webpage and www.BRINKClaimsworks.com. I can send our logo as well.
Updates

Looking for something elegant but industrial, rustic and modern. Added Sunday, June 4, 2017

Industry/Entity Type

Insurance

Font styles to use
Serif

Requirements
Must have
• Contact information

```html
<!DOCTYPE html>
<html lang="en">
<head>
<meta charset="utf-8">
<title>BRINK Claimsworks – Full Page Ad</title>
<link href="https://fonts.googleapis.com/css2?family=Lato:ital,wght@0,400;0,700;0,900;1,700&display=swap" rel="stylesheet">
<style>
  :root {
    --navy: #2b3a67;
    --orange: #e8772e;
    --orange-deep: #d9642a;
    --ink: #2a1a0e;
    --white: #ffffff;
    --page-bg: #f2f2f2;
    --fire-yellow: #f7c33a;
    --fire-orange: #e87a1f;
    --fire-deep: #c9501a;
    --grass: #5f7a32;
    --hose-red: #d8332b;
  }
  * { box-sizing: border-box; margin: 0; padding: 0; }
  html, body { width: 1200px; height: 1200px; overflow: hidden; }
  body {
    background: var(--page-bg);
    font-family: "Lato", sans-serif;
    position: relative;
  }
  .ad {
    position: absolute;
    left: 202px; top: 38px;
    width: 796px; height: 1125px;
    background: var(--white);
    overflow: hidden;
  }
  .service-bar {
    position: absolute; left: 0; top: 0; width: 100%; height: 68px;
    background: var(--navy);
    display: flex; align-items: center; justify-content: center;
    gap: 18px;
    font-weight: 900; font-size: 15px; letter-spacing: 3.6px;
    color: var(--white);
  }
  .service-bar .accent { color: var(--orange); }
  .service-bar .sep { font-weight: 400; opacity: .8; }
  .hero {
    position: absolute; left: 0; top: 78px; width: 100%; height: 914px;
  }
  .hero-photo {
    position: absolute; inset: 0;
    background:
      linear-gradient(180deg, transparent 84%, rgba(95,122,50,.85) 90%, var(--grass) 100%),
      radial-gradient(ellipse at 80% 10%, #fde57a 0%, transparent 55%),
      radial-gradient(ellipse at 15% 35%, var(--fire-deep) 0%, transparent 55%),
      linear-gradient(180deg, var(--fire-yellow) 0%, var(--fire-orange) 45%, #d98a45 75%, #b7783f 84%);
  }
  .hero-rule {
    position: absolute; left: 0; bottom: 0; width: 100%; height: 6px;
    background: var(--hose-red);
  }
  .tagline {
    position: absolute; right: 52px; top: 66px;
    font-style: italic; font-weight: 700; font-size: 21px;
    color: var(--orange-deep);
  }
  .headline {
    position: absolute; left: 122px; top: 195px;
    font-weight: 900; font-size: 71px; letter-spacing: -1px;
    color: var(--white);
    text-shadow: 0 3px 8px rgba(80,30,0,.55);
  }
  .perils {
    position: absolute; left: 122px; top: 279px;
    font-weight: 700; font-size: 21px; color: var(--ink);
  }
  .intro {
    position: absolute; left: 122px; top: 330px; width: 390px;
    font-weight: 700; font-size: 15px; line-height: 21.6px; color: var(--ink);
  }
  .services-panel {
    position: absolute; left: 0; top: 651px; width: 100%; height: 172px;
    background: linear-gradient(90deg, rgba(232,119,46,.92) 0%, rgba(232,119,46,.85) 38%, rgba(232,119,46,.35) 60%, transparent 78%);
    padding: 24px 0 0 48px;
    color: var(--white);
  }
  .services-panel h2 {
    font-weight: 900; font-size: 22px; line-height: 24px;
  }
  .services-panel p {
    margin-top: 12px; width: 360px;
    font-weight: 400; font-size: 14px; line-height: 17.6px;
  }
  .footer {
    position: absolute; left: 0; bottom: 0; width: 100%; height: 121px;
    background: var(--navy);
    color: var(--white);
  }
  .brand-name {
    position: absolute; left: 48px; top: 28px;
    font-weight: 900; font-size: 46px; letter-spacing: 1px;
    color: var(--white);
  }
  .divider {
    position: absolute; top: 32px; width: 1.5px; height: 50px;
    background: rgba(255,255,255,.8);
  }
  .divider.first { left: 252px; }
  .divider.second { left: 498px; }
  .contact {
    position: absolute; left: 267px; top: 30px;
    font-size: 11px; line-height: 13.3px; font-weight: 400;
  }
  .contact b { font-weight: 700; }
  .call {
    position: absolute; left: 514px; top: 28px;
    font-weight: 900; line-height: 1;
  }
  .call .label { font-size: 28px; color: var(--white); }
  .call .number { font-size: 29px; color: var(--orange); margin-top: 2px; }
</style>
</head>
<body>
  <main class="ad">
    <header class="service-bar">
      <span class="accent">24/7 CLAIM SERVICE</span>
      <span class="sep">|</span>
      <span>FAST REPORTING</span>
      <span class="sep">|</span>
      <span>PREMIUM QUALITY</span>
    </header>

    <section class="hero">
      <div class="hero-photo" role="img" aria-label="Firefighters in protective gear with air tanks holding a red hose in front of a large blaze on a grassy field"></div>
      <div class="hero-rule"></div>
      <p class="tagline">Committed to satisfying your needs.</p>
      <h1 class="headline">When It Happens</h1>
      <p class="perils">Accidents, Disasters, Fire, Flood, Wind, Property &amp; Liability</p>
      <p class="intro">BRINK retains the benefits of a large firm in our capacity to handle high volume and complex claims over a large geographical area while at the same time retaining flexibility and personal tailored service.</p>
      <div class="services-panel">
        <h2>Independent Claim<br>Adjusters &amp; Administration</h2>
        <p>With 12 locations throughout the North East we are able to service all of New York State as well as servicing Vermont, Western Massachusetts, Connecticut, Northern New Jersey and Pennsylvania.</p>
      </div>
    </section>

    <footer class="footer">
      <div class="brand-name">BRINK</div>
      <div class="divider first"></div>
      <address class="contact" style="font-style:normal">
        Home Office: <b>PO Box 318</b><br>
        <b>210 Mill Street Riverton, NY 12099</b><br>
        Phone: <b>518-555-0148</b> | Fax: <b>888-555-0173</b><br>
        <b>www.BRINKClaimsworks.com</b>
      </address>
      <div class="divider second"></div>
      <div class="call">
        <div class="label">CALL</div>
        <div class="number">1-800-555-0162</div>
      </div>
    </footer>
  </main>
</body>
</html>
```